RW Hollis LLC Business Card - Civil Engineering & Consulting Firm

We need a Business Card that is elegant, and masculine.  It is our Professional Civil Engineering & Consulting Company located in San Antonio TX (Not s construction or builder firm- no gears & no tool images please). We provide civil engineering services including  commercial site plans, grading and drainage plans, utility plans, hydraulics and hydrology, land planning, utility coordination, and other general civil engineering services related to commercial and residential development.
We have 2 existing Logos. We would like to convey reliability, strength, trustworthiness and attention to detail.  Blues and orange tones as per logo We are OK with the use of a darker blue in the mix.  We have 2 logo versions - Full Company Name Logo to go on the back of card, & Small Icon Logo for the front w/ personal Info.

Target Market(s)
Architects, Real Estate Developers, Other Strctural Engineers, Surveyers, General Contractors
Industry/Entity Type
Professional Civil Engineering
Contact Information for Business Card
Name, Position, Address, Cell & Office #, email, and company website
Font styles to use
Other font styles liked:
- Avian
Requirements
Should not have
- No Tools, No Gears, no Cranes, or Construction Equipment.

```html
<!DOCTYPE html>
<html lang="en">
<head>
<meta charset="utf-8">
<title>RW Hollis LLC – Business Card</title>
<link rel="stylesheet" href="https://fonts.googleapis.com/css2?family=Montserrat:wght@300;400;500;700&display=swap">
<style>
  :root {
    --stage: #b9b9b9;
    --card-light: #f1f0f1;
    --card-shade: #dedcde;
    --ink: #1e1e1e;
    --orange: #ef8f2c;
    --blue: #7aa9d3;
    --back-blue: #7b9fbd;
    --back-mid: #a5978c;
    --back-orange: #e0954a;
    --white: #ffffff;
  }
  * { margin: 0; padding: 0; box-sizing: border-box; }
  html, body { width: 1200px; height: 813px; overflow: hidden; }
  body {
    background: var(--stage);
    font-family: "Montserrat", sans-serif;
    position: relative;
  }
  .card {
    position: absolute;
    top: 251px;
    width: 540px;
    height: 310px;
    overflow: hidden;
    box-shadow: 0 10px 26px rgba(0,0,0,0.28);
  }

  /* Front */
  .card--front {
    left: 30px;
    background:
      linear-gradient(120deg, transparent 0 55%, rgba(255,255,255,0.45) 55% 75%, transparent 75%),
      linear-gradient(35deg, var(--card-shade) 0 30%, transparent 30%),
      linear-gradient(160deg, var(--card-light), #e4e3e5);
  }
  .brand-mark {
    position: absolute;
    left: 40px;
    top: 122px;
    display: flex;
    align-items: center;
    gap: 10px;
    font-weight: 700;
    font-size: 22px;
    color: var(--orange);
    letter-spacing: 0.02em;
    white-space: nowrap;
  }
  .brand-mark__square {
    width: 16px; height: 16px;
    background: var(--blue);
  }
  .identity {
    position: absolute;
    left: 40px;
    bottom: 34px;
  }
  .identity__name {
    font-weight: 700;
    font-size: 17px;
    color: var(--orange);
    letter-spacing: 0.03em;
  }
  .identity__role {
    font-weight: 400;
    font-size: 14px;
    color: var(--ink);
    margin-top: 4px;
  }
  .contact {
    position: absolute;
    left: 340px;
    top: 34px;
    width: 175px;
    font-size: 12.5px;
    color: var(--ink);
    line-height: 1.5;
    white-space: nowrap;
  }
  .contact__address { margin-bottom: 14px; }
  .contact__list { list-style: none; }
  .contact__item { display: flex; align-items: center; gap: 8px; margin-bottom: 2px; }
  .contact__icon { width: 13px; height: 13px; flex: none; }

  /* Back */
  .card--back {
    left: 630px;
    background:
      linear-gradient(115deg, rgba(255,255,255,0.08) 0 40%, transparent 40%),
      linear-gradient(160deg, var(--back-blue) 0%, var(--back-mid) 45%, var(--back-orange) 100%);
    color: var(--white);
  }
  .wordmark {
    position: absolute;
    left: 0; right: 0;
    top: 96px;
    text-align: center;
  }
  .wordmark__name {
    display: inline-flex;
    align-items: center;
    gap: 14px;
    font-weight: 300;
    font-size: 46px;
    letter-spacing: 0.08em;
  }
  .wordmark__square {
    width: 14px; height: 14px;
    background: var(--white);
  }
  .wordmark__rule {
    width: 380px;
    height: 2px;
    background: var(--white);
    margin: 12px auto 10px;
  }
  .wordmark__tagline {
    font-weight: 400;
    font-size: 13px;
    letter-spacing: 0.42em;
  }
</style>
</head>
<body>
  <section class="card card--front" aria-label="Business card front">
    <div class="brand-mark">
      <span class="brand-mark__square"></span>
      <span>RW Hollis LLC</span>
    </div>

    <div class="identity">
      <p class="identity__name">DANE WHITCOMBE</p>
      <p class="identity__role">Co-Founder</p>
    </div>

    <div class="contact">
      <p class="contact__address">4180 N. Ridge Avenue<br>Suite 210 Alamo 12</p>
      <ul class="contact__list">
        <li class="contact__item">
          <svg class="contact__icon" viewBox="0 0 16 16"><path d="M3 1h3l1.5 4-2 1.2a9 9 0 0 0 4.3 4.3L11 8.5l4 1.5v3a2 2 0 0 1-2 2A12 12 0 0 1 1 3a2 2 0 0 1 2-2z" fill="var(--orange)"/></svg>
          <span>555-214-0381</span>
        </li>
        <li class="contact__item">
          <svg class="contact__icon" viewBox="0 0 16 16"><rect x="2" y="6" width="12" height="9" rx="1.5" fill="var(--orange)"/><rect x="1" y="2" width="14" height="3" rx="1.5" fill="var(--orange)"/></svg>
          <span>555-214-0492</span>
        </li>
        <li class="contact__item">
          <svg class="contact__icon" viewBox="0 0 16 16"><rect x="1" y="3" width="14" height="10" fill="var(--orange)"/><path d="M1 3l7 6 7-6" fill="none" stroke="#fff" stroke-width="1.4"/></svg>
          <span>info@rwhollisllc</span>
        </li>
        <li class="contact__item">
          <svg class="contact__icon" viewBox="0 0 16 16"><circle cx="8" cy="8" r="7" fill="var(--orange)"/><path d="M1 8h14M8 1c-3 3.5-3 10.5 0 14M8 1c3 3.5 3 10.5 0 14" fill="none" stroke="#fff" stroke-width="1"/></svg>
          <span>www.rwhollisllc.com</span>
        </li>
      </ul>
    </div>
  </section>

  <section class="card card--back" aria-label="Business card back">
    <div class="wordmark">
      <p class="wordmark__name"><span class="wordmark__square"></span>RW Hollis LLC</p>
      <div class="wordmark__rule"></div>
      <p class="wordmark__tagline">CONSULTING ENGINEERS</p>
    </div>
  </section>
</body>
</html>
```